Grain Clear Kitchen Web Design

We are looking for designs for a homepage for a gluten free, health food website.

We are looking for the site to be a shop, as well as a resource/information source for users. We will also look to incorporate recipes, blogs, forums and potentially some other useful information.

We want to ensure that the website is user-friendly, does not have a corporate feel, but is still classy.

We want to have high quality photographic images in the background, with text in the foreground - but these things will need to compliment each other well. e.g recipe of the week integrated onto the background photo and the 'shop' in the foreground.

We have seen a site that we quite like and although we like the design, we do not want to completely emulate this. However, it is a useful starting point for designers and perhaps some inspiration www.brightpantryhall.example

We already have a logo - see attached - which will need to be fully integrated into the design.

We do want a colourful design, but mainly in terms of the images rather than the graphics.
Updates

Please note:

We are pleased with the designs to date, for the most part. We would like you all to note, however, that we are much preferring the lighter designs - ones that make the sites feel brighter - rather than those which are darker in appearance.

We would also like to see less space allocated to the main image, within the context of the site as a whole.

Thanks.

We have eliminated those which we feel are not what we are looking for. We are still keen to see some more designs and are still looking for something unique. There are some good things in all of the designs that we have not eliminated, however we still feel there is room for more inspiration.

Thanks.

Target Market(s)

Our audience are body conscience people looking for health food products. They are also those who are potentially looking for a new lifestyle/life cha

Industry/Entity Type

Health

Requirements
Must have
• Our logo - attached, can provide variations in due course.

Navigational features as per mock up attached.

Social network integration.

NB: we only need one (home) page for this.

```html
<!DOCTYPE html>
<html lang="en">
<head>
<meta charset="utf-8">
<title>Grain Clear Kitchen</title>
<link rel="stylesheet" href="https://fonts.googleapis.com/css2?family=Kaushan+Script&family=Courgette&family=Open+Sans:wght@400;600;700&family=Archivo+Black&display=swap">
<style>
:root{
  --orange:#e8820c;
  --orange-light:#f6a21a;
  --charcoal:#454545;
  --panel:#3a3a3a;
  --cream:#f4efe3;
  --ink:#4a4a4a;
  --white:#ffffff;
  --dark-btn:#222222;
}
*{margin:0;padding:0;box-sizing:border-box}
html,body{width:928px;height:1200px;overflow:hidden}
body{position:relative;background:var(--charcoal);font-family:"Open Sans",sans-serif;color:var(--ink)}

.hero{position:absolute;left:0;top:0;width:928px;height:498px;
  background:radial-gradient(circle at 30% 40%,#f39a2a 0,transparent 22%),
             radial-gradient(circle at 70% 30%,#d8283a 0,transparent 20%),
             radial-gradient(circle at 55% 75%,#e23a48 0,transparent 24%),
             radial-gradient(circle at 20% 80%,#2a1d2a 0,transparent 20%),
             radial-gradient(circle at 85% 70%,#f08a1c 0,transparent 22%),
             linear-gradient(135deg,#8b6a3e,#c8463a 45%,#6f8a4a)}
.topbar{position:absolute;left:0;top:0;width:928px;height:38px;background:rgba(40,40,40,.55)}
.topnav{position:absolute;left:478px;top:11px;display:flex;gap:7px;font-size:10px;color:var(--white);letter-spacing:.3px}
.topnav span.sep{opacity:.8}
.search{position:absolute;left:650px;top:5px;width:184px;height:27px;border-radius:14px;background:rgba(30,30,30,.7);border:1px solid rgba(255,255,255,.15)}
.search svg{position:absolute;left:9px;top:7px}
.search::after{content:"";position:absolute;left:27px;top:4px;width:1px;height:19px;background:rgba(255,255,255,.2)}

.sidebar{position:absolute;left:35px;top:0;width:196px;height:358px;background:var(--panel);box-shadow:2px 2px 8px rgba(0,0,0,.4)}
.brand{position:absolute;left:0;top:36px;width:196px;display:flex;align-items:center;justify-content:center;gap:8px;color:var(--white);font-weight:700;font-size:17px;line-height:1.15}
.brand-dot{width:14px;height:14px;border-radius:50%;background:var(--white);flex:none}
.menu{position:absolute;left:0;top:168px;width:196px;list-style:none}
.menu li{height:31px;border-top:1px dashed #1f1f1f;box-shadow:inset 0 1px 0 rgba(255,255,255,.06);font-family:"Courgette",cursive;color:#d8d8d8;font-size:14px;padding:6px 0 0 25px}

.hero-copy{position:absolute;left:316px;top:142px;width:440px;text-align:center}
.hero-title{font-family:"Kaushan Script",cursive;font-size:46px;line-height:56px;color:var(--orange-light);
  text-shadow:-2px -2px 0 #fff,2px -2px 0 #fff,-2px 2px 0 #fff,2px 2px 0 #fff,3px 4px 6px rgba(0,0,0,.5)}
.hero-sub{margin-top:14px;font-family:"Archivo Black",sans-serif;font-size:12.5px;line-height:17px;color:var(--orange-light);text-transform:uppercase;
  text-shadow:-1px -1px 0 #fff,1px -1px 0 #fff,-1px 1px 0 #fff,1px 1px 0 #fff}
.btn-prices{position:absolute;left:491px;top:328px;width:86px;height:30px;border-radius:15px;background:var(--orange);color:var(--white);font-size:10px;font-weight:600;display:flex;align-items:center;justify-content:center;box-shadow:0 2px 4px rgba(0,0,0,.4)}
.dots{position:absolute;left:507px;top:404px;display:flex;gap:12px}
.dots i{width:12px;height:12px;border-radius:50%;border:2px solid var(--white);background:var(--orange)}
.dots i:first-child{background:#555;border-color:#777}

.cards{position:absolute;left:93px;top:513px;display:grid;grid-template-columns:repeat(3,232px);grid-auto-rows:248px;gap:23px}
.card{position:relative;background:var(--cream);padding:0 8px;box-shadow:6px 10px 12px -6px rgba(0,0,0,.6)}
.card h2{font-family:"Kaushan Script",cursive;font-weight:400;font-size:22px;color:var(--orange);height:46px;padding:7px 0 0 2px}
.card-photo{height:100px;width:217px}
.card h3{margin-top:8px;font-size:11px;font-weight:600;color:var(--orange)}
.card p{margin-top:3px;font-size:8.6px;line-height:12px;text-align:justify}
.card .addr{color:var(--orange);font-size:8px;line-height:11px;text-align:left;margin-top:8px}
.more{position:absolute;left:8px;top:213px;width:78px;height:25px;background:var(--orange);color:var(--white);font-size:9px;display:flex;align-items:center;justify-content:center;gap:6px}

.newsletter{position:absolute;left:93px;top:1069px;width:742px;height:59px;background:var(--orange)}
.newsletter h2{position:absolute;left:14px;top:18px;font-family:"Archivo Black",sans-serif;font-weight:400;font-size:15.5px;color:#fde1bd;letter-spacing:.2px}
.field{position:absolute;top:14px;width:210px;height:28px;background:#efefef;font-size:9px;color:#444;padding:8px 0 0 12px}
.field.name{left:207px}
.field.email{left:432px}
.signup{position:absolute;left:661px;top:14px;width:70px;height:28px;background:var(--dark-btn);color:var(--white);font-family:"Archivo Black",sans-serif;font-size:11px;display:flex;align-items:center;justify-content:center}

.footer{position:absolute;left:88px;top:1150px;font-family:"Archivo Black",sans-serif;font-size:9px;line-height:13px;color:#cfcfcf}
.social{position:absolute;left:716px;top:1148px;display:flex;gap:7px}
.social i{width:24px;height:24px;background:#2a2a2a}
</style>
</head>
<body>
<header class="hero" role="img" aria-label="Photo of a glass bowl filled with mixed fresh fruit: berries and mandarin segments"></header>
<div class="topbar"></div>
<nav class="topnav"><span>HOME</span><span class="sep">|</span><span>LOGIN</span><span class="sep">|</span><span>CONTACT US</span></nav>
<div class="search"><svg width="11" height="11" viewBox="0 0 11 11"><circle cx="4.5" cy="4.5" r="3.3" fill="none" stroke="#bbb" stroke-width="1.4"/><line x1="7" y1="7" x2="10" y2="10" stroke="#bbb" stroke-width="1.6"/></svg></div>

<aside class="sidebar">
  <div class="brand"><span class="brand-dot"></span><span>Grain Clear<br>Kitchen</span></div>
  <ul class="menu">
    <li>Shop</li><li>Our Story</li><li>Blog</li><li>Hints &amp; Tips</li><li>Recipes</li><li>Forums</li>
  </ul>
</aside>

<section class="hero-copy">
  <h1 class="hero-title">Voluptatem ac<br>Tum Doloremque</h1>
  <p class="hero-sub">Voluptatem accusantium doloremque laudantium, totam rem aperiam, eaque ipsa quae ab illo inventore veritatis et quasi architecto beatae vitae dicta</p>
</section>
<div class="btn-prices">GET PRICES</div>
<div class="dots"><i></i><i></i><i></i></div>

<main class="cards">
  <article class="card">
    <h2>Our Shop</h2>
    <div class="card-photo" role="img" aria-label="Shop assistant beside a fruit display" style="background:linear-gradient(90deg,#7fb83a,#d9c34a 45%,#e8e2d8 70%,#f2ede6)"></div>
    <p class="addr">Orchard Row, Millbrook MB4 2QT<br>Phone: (000)55501234<br>Hours: 8am to 9pm Monday to Saturday, 9am to 9pm Sunday</p>
    <div class="more">MORE INFO <svg width="11" height="9" viewBox="0 0 11 9"><path d="M0 4.5h9M6 1l3.5 3.5L6 8" fill="none" stroke="#fff" stroke-width="1.5"/></svg></div>
  </article>
  <article class="card">
    <h2>Voluptatum</h2>
    <div class="card-photo" role="img" aria-label="Apples, oranges and grapefruit" style="background:linear-gradient(90deg,#e07a3a,#7fae3a 35%,#b8302c 65%,#e8923a)"></div>
    <h3>Perspiciatis unde</h3>
    <p>omnis iste natus error sit voluptatem accusantium doloremque laudantium, totam rem aperiam, eaque ipsa quae ab illo inventore veritatis et quasi</p>
    <div class="more">MORE INFO <svg width="11" height="9" viewBox="0 0 11 9"><path d="M0 4.5h9M6 1l3.5 3.5L6 8" fill="none" stroke="#fff" stroke-width="1.5"/></svg></div>
  </article>
  <article class="card">
    <h2>Blanditiis</h2>
    <div class="card-photo" role="img" aria-label="Apricots on a wooden board" style="background:linear-gradient(90deg,#6f6658,#e8963a 40%,#f0a24a 70%,#8a7a68)"></div>
    <h3>Perspiciatis unde</h3>
    <p>omnis iste natus error sit voluptatem accusantium doloremque laudantium, totam rem aperiam, eaque ipsa quae ab illo inventore veritatis et quasi</p>
    <div class="more">MORE INFO <svg width="11" height="9" viewBox="0 0 11 9"><path d="M0 4.5h9M6 1l3.5 3.5L6 8" fill="none" stroke="#fff" stroke-width="1.5"/></svg></div>
  </article>
  <article class="card">
    <h2>indignation</h2>
    <div class="card-photo" role="img" aria-label="Halved oranges, grapefruit and kiwi" style="background:linear-gradient(90deg,#f0a020,#e05a2a 50%,#f0c030)"></div>
    <h3>Perspiciatis unde</h3>
    <p>omnis iste natus error sit voluptatem accusantium doloremque laudantium, totam rem aperiam, eaque ipsa quae ab illo inventore veritatis et quasi</p>
    <div class="more">MORE INFO <svg width="11" height="9" viewBox="0 0 11 9"><path d="M0 4.5h9M6 1l3.5 3.5L6 8" fill="none" stroke="#fff" stroke-width="1.5"/></svg></div>
  </article>
  <article class="card">
    <h2>demoralized</h2>
    <div class="card-photo" role="img" aria-label="Fruit salad with strawberries and kiwi" style="background:linear-gradient(90deg,#f0d070,#e04a3a 45%,#f2e090 75%,#8fa04a)"></div>
    <h3>Perspiciatis unde</h3>
    <p>omnis iste natus error sit voluptatem accusantium doloremque laudantium, totam rem aperiam, eaque ipsa quae ab illo inventore veritatis et quasi</p>
    <div class="more">MORE INFO <svg width="11" height="9" viewBox="0 0 11 9"><path d="M0 4.5h9M6 1l3.5 3.5L6 8" fill="none" stroke="#fff" stroke-width="1.5"/></svg></div>
  </article>
  <article class="card">
    <h2>denouncing</h2>
    <div class="card-photo" role="img" aria-label="Diced melon, kiwi, strawberries and cherries" style="background:linear-gradient(90deg,#c8d87a,#8fbf3a 40%,#e0402a 70%,#5a1a20)"></div>
    <h3>Perspiciatis unde</h3>
    <p>omnis iste natus error sit voluptatem accusantium doloremque laudantium, totam rem aperiam, eaque ipsa quae ab illo inventore veritatis et quasi</p>
    <div class="more">MORE INFO <svg width="11" height="9" viewBox="0 0 11 9"><path d="M0 4.5h9M6 1l3.5 3.5L6 8" fill="none" stroke="#fff" stroke-width="1.5"/></svg></div>
  </article>
</main>

<section class="newsletter">
  <h2>NEWSLETTER SIGNUP</h2>
  <div class="field name">Enter Your Name</div>
  <div class="field email">Enter Email Address</div>
  <div class="signup">SIGN UP</div>
</section>

<footer class="footer">
  <div>SHOP &nbsp;|&nbsp; OUR STORY &nbsp;|&nbsp; BLOG &nbsp;|&nbsp; HINTS &amp; TIPS &nbsp;|&nbsp; RECIPES &nbsp;|&nbsp; FORUMS</div>
  <div>© 2013 GRAIN CLEAR KITCHEN. | ALL RIGHTS RESERVED.</div>
</footer>
<div class="social" aria-label="Social links"><i></i><i></i><i></i><i></i></div>
</body>
</html>
```